ホームページもご確認ください。
https://milfone-salon.example/

女性だけの会社です。
産休育休制度に力をいれています。
イメージ
https://kyujin.tobiume-tetsudo.example/company/life-style/vol6.html

産休育休制度は1枚切り取って他の資料にも使えるようにしていただきたいです。

いただいたデータはヨルテンで印刷を依頼するので、
ヨルテン入稿できる方法のデータでお願いします。
またHPにもリンクします。
A4
8ページ
無彩色系
◆ミルフォネはどんな会社?
<概要>
アイラッシュ、ネイル、エステ、脱毛サロンを石川県内で3店舗経営しています。
創業以来、従業員ファーストの視点で経営をしてきました。
来年で10周年を迎える、従業員23名の小さなサロンです。

<働き方>
石川県はたらく灯し火アワードを受賞。
完全週休2日制に加え、週休3日制を導入。さらに、新たな雇用形態のしてフリーランス契約を開始しました。
時代に合った新しい働き方をいち早く導入できる柔軟な会社です。

<スピード>
新技術、新商品をいち早く導入。
時代のニーズを汲み取り、流行を先取りしています。
また、トップダウン方式で意思決定スピードも超高速です。

<福利厚生>
社保完備。
2年に1回、全額会社負担で社員旅行を実施しています。(昨年はハワイ)
従業員はすべて女性です。働く女性を会社が支えられるように産休・育休を積極的に取得を心がけています。
さらに、家庭、子育て、介護と仕事を両立していけるような仕組みを作ること、それを今後の会社の課題として取り組んでいきます。
フリーランス募集用に撮影したモデルの写真です。
+Ri内装写真を追加します。
mirvane内装写真を追加します。
solverine内装写真を追加します。
会社名・店舗名のロゴを追加します。
手書き案ですが、パンフレットの構成を追加します。

1ページ
2ページ
フリーランスモデルの写真を使ってデザインしてください。

3ページ
内容はそのままでデザインをお願いします。

4ページ
基本内容はそのままですが先輩社員の一日の内容が薄いので
肉付けしたいです。

5ページ
採用の箇所にLINEも追加してください。

6ページ
内容そのまま

7ページ
ここは産休・育休の専用ページを考えております。
デザイン、構成をお願いします。

8ページ
7ページ、8ページを入れ替えてエントリー方法、会社概要としてください。
エントリー方法はLINEを追加
ミルフォネの社名の由来修正
をお願いします。

ざっくりとで申し訳ございませんが、よろしくお願いします。

夜分遅くにすみません。
素敵なデザインありがとうございます!
取り急ぎご連絡まて。。

レスポンスは大切りにしています!
よろしくお願いいたします!

```html
<!DOCTYPE html>
<html lang="ja">
<head>
<meta charset="utf-8">
<title>MILFONE Recruit Information</title>
<link rel="stylesheet" href="https://fonts.googleapis.com/css2?family=Cormorant+Garamond:ital,wght@0,300;0,400;0,500;1,300&family=Noto+Serif+JP:wght@300;400&display=swap">
<style>
  :root {
    --paper: #e8dcd6;
    --paper-light: #f1e9e5;
    --panel: #f7f3f1;
    --ink: #5a4f4c;
    --ink-soft: #8a7f7b;
    --title-light: #f6f1ee;
    --line: rgba(255, 255, 255, 0.7);
  }
  * { margin: 0; padding: 0; box-sizing: border-box; }
  html, body { width: 842px; height: 1200px; overflow: hidden; background: var(--paper); }
  .cover {
    position: relative;
    width: 842px;
    height: 1200px;
    overflow: hidden;
    background: linear-gradient(160deg, var(--paper-light) 0%, var(--paper) 55%, #e4d6cf 100%);
  }
  .accent-lines { position: absolute; inset: 0; }
  .flower-art {
    position: absolute;
    left: 20px; top: -20px;
    width: 270px; height: 230px;
    border-radius: 50%;
    background: radial-gradient(circle at 50% 50%, rgba(255,255,255,0.55) 0%, rgba(240,228,222,0.35) 55%, rgba(232,220,214,0) 75%);
  }
  .leaf-art {
    position: absolute;
    right: 10px; bottom: 0;
    width: 240px; height: 170px;
    background: radial-gradient(ellipse at 60% 60%, rgba(196,206,186,0.55) 0%, rgba(214,218,200,0.3) 50%, rgba(232,220,214,0) 75%);
  }
  .hero-photo {
    position: absolute;
    left: 174px; top: 175px;
    width: 668px; height: 583px;
    background: linear-gradient(90deg, #f3efec 0%, #d9ccc4 30%, #c7b2a4 55%, #b49a88 75%, #d6c8be 100%);
  }
  .brand {
    position: absolute;
    left: 112px; top: 292px;
    color: var(--ink);
  }
  .brand-company {
    font-family: "Noto Serif JP", serif;
    font-weight: 400;
    font-size: 11px;
    letter-spacing: 0.08em;
  }
  .brand-name {
    font-family: "Cormorant Garamond", serif;
    font-weight: 400;
    font-size: 56px;
    letter-spacing: 0.06em;
    line-height: 1.05;
    margin-top: 4px;
  }
  .brand-tagline {
    font-family: "Noto Serif JP", serif;
    font-weight: 300;
    font-size: 13px;
    letter-spacing: 0.1em;
    margin-top: 12px;
  }
  .title {
    position: absolute;
    right: 66px; top: 900px;
    text-align: right;
  }
  .title-script {
    font-family: "Cormorant Garamond", serif;
    font-style: italic;
    font-weight: 300;
    font-size: 54px;
    color: var(--title-light);
    letter-spacing: 0.08em;
    line-height: 1;
  }
  .title-main {
    font-family: "Cormorant Garamond", serif;
    font-weight: 400;
    font-size: 46px;
    color: var(--ink-soft);
    letter-spacing: 0.16em;
    margin-top: 18px;
  }
</style>
</head>
<body>
  <main class="cover">
    <svg class="accent-lines" width="842" height="1200" viewBox="0 0 842 1200" aria-hidden="true">
      <line x1="400" y1="0" x2="842" y2="150" stroke="var(--line)" stroke-width="1.5"/>
      <line x1="560" y1="1200" x2="842" y2="1080" stroke="var(--line)" stroke-width="1"/>
    </svg>
    <div class="flower-art" role="img" aria-label="淡いピンクの花のイラスト"></div>
    <div class="hero-photo" role="img" aria-label="笑顔の女性モデルの写真"></div>
    <div class="brand">
      <p class="brand-company">株式会社ミルフォネ</p>
      <p class="brand-name">MILFONE</p>
      <p class="brand-tagline">リクルートインフォメーション</p>
    </div>
    <div class="title">
      <p class="title-script">Recruit</p>
      <p class="title-main">INFORMATION</p>
    </div>
    <div class="leaf-art" role="img" aria-label="淡い緑の葉のイラスト"></div>
  </main>
</body>
</html>
```